Packaging Design for Boneless Picnic Ham

We are Tidewell Provisions Limited, a company based in Trinidad which is located within the Caribbean. We produce and sell a plethora of meat products including a variety of hams, sausages and even bacon.

We require a packaging design for a ham product. This product is packaged within a cryovac (11" X 18") shrink bag which would be used to package our Boneless Picnic Ham which weighs 2.5 Kilograms.

The design space should be 7 inches wide and 6 inches in height. The design is 3 inches from the bottom and 2 inches off each side.

Our target audience comprises of caterers as well as the average household folk. What sets our product apart is that it is has a great taste, 20% less salt and is affordable and easy. We commonly refer to it as the "Sunday Roast Joint".

Attached below, is our logo which you must incorporate onto the design. We also request that the header be "Hickory Smoked Boneless Picnic Ham".

Target Market(s)

Caterers and Average Household Folk

Font styles to use
Sans Serif

Requirements
Must have
• The Tidewell Provisions Company Logo and the header must have "Hickory Smoked Boneless Picnic Ham"
Nice to have
• Maximum Creativity
Should not have
• No animal artwork should be included onto the design

```html
<!DOCTYPE html>
<html lang="en">
<head>
<meta charset="utf-8">
<title>Tidewell Provisions – Hickory Smoked Boneless Picnic Ham</title>
<link rel="stylesheet" href="https://fonts.googleapis.com/css2?family=Fira+Sans:ital,wght@0,200;0,300;0,400;0,700;0,800;1,300&display=swap">
<style>
  :root {
    --navy: #1e2a6b;
    --gold: #f2dc8a;
    --tab-yellow: #f7dc73;
    --white: #ffffff;
    --page: #f4f4f2;
  }
  html, body {
    margin: 0;
    padding: 0;
    overflow: hidden;
  }
  body {
    width: 1200px;
    height: 1200px;
    background: var(--page);
    position: relative;
  }
  .pack-label {
    position: absolute;
    left: 320px;
    top: 90px;
    width: 560px;
    height: 1032px;
  }
  .brand-tab { fill: var(--tab-yellow); }
  .label-border { fill: var(--white); }
  .label-panel { fill: var(--navy); }
  .brand-name {
    font-family: "Fira Sans", sans-serif;
    font-weight: 800;
    font-size: 15px;
    fill: var(--navy);
  }
  .title-frame, .weight-frame {
    fill: none;
    stroke: var(--white);
    stroke-width: 1.6;
  }
  .title-line-1 {
    font-family: "Fira Sans", sans-serif;
    font-weight: 300;
    font-size: 20px;
    fill: var(--white);
  }
  .title-line-2 {
    font-family: "Fira Sans", sans-serif;
    font-weight: 300;
    font-size: 28px;
    letter-spacing: 3px;
    fill: var(--gold);
  }
  .title-line-3 {
    font-family: "Fira Sans", sans-serif;
    font-weight: 700;
    font-size: 31px;
    fill: var(--white);
  }
  .cook-note {
    font-family: "Fira Sans", sans-serif;
    font-weight: 400;
    font-size: 11px;
    letter-spacing: 3px;
    fill: var(--gold);
  }
  .divider {
    stroke: var(--white);
    stroke-width: 0.6;
    opacity: 0.7;
  }
  .benefits {
    font-family: "Fira Sans", sans-serif;
    font-style: italic;
    font-weight: 300;
    font-size: 10px;
    letter-spacing: 0.8px;
    fill: var(--white);
  }
  .weight-value {
    font-family: "Fira Sans", sans-serif;
    font-weight: 700;
    font-size: 22px;
    fill: var(--gold);
  }
  .weight-unit {
    font-family: "Fira Sans", sans-serif;
    font-weight: 400;
    font-size: 9px;
    fill: var(--white);
  }
</style>
</head>
<body>
  <svg class="pack-label" viewBox="0 -10 350 645" xmlns="http://www.w3.org/2000/svg">
    <path class="brand-tab" d="M88,22 L305,-4 L280,100 L150,88 Z"/>
    <path class="label-border" d="M25,28 H325 Q350,28 350,53 V605 Q350,630 325,630 H200 Q176,630 170,606 C152,530 128,485 84,462 C40,440 0,430 0,390 V53 Q0,28 25,28 Z"/>
    <path class="label-panel" d="M40,50 H325 Q337,50 337,62 V593 Q337,605 325,605 H200 Q188,605 184,592 C166,518 140,468 92,444 C50,424 15,418 15,385 V75 Q15,50 40,50 Z"/>

    <text class="brand-name" x="233" y="24" text-anchor="middle">Tidewell</text>
    <text class="brand-name" x="233" y="42" text-anchor="middle">Provisions</text>

    <rect class="title-frame" x="45" y="137" width="262" height="171"/>
    <text class="title-line-1" x="178" y="190" text-anchor="middle">Hickory Smoked</text>
    <text class="title-line-2" x="178" y="223" text-anchor="middle">BONELESS</text>
    <text class="title-line-3" x="178" y="260" text-anchor="middle">Picnic Ham</text>

    <text class="cook-note" x="178" y="342" text-anchor="middle">EASY BAKE</text>
    <line class="divider" x1="45" y1="356" x2="307" y2="356"/>
    <text class="benefits" x="178" y="381" text-anchor="middle">Great Taste ·  20% less salt</text>

    <rect class="weight-frame" x="232" y="493" width="76" height="80"/>
    <text class="weight-value" x="270" y="533" text-anchor="middle">2,5</text>
    <text class="weight-unit" x="270" y="557" text-anchor="middle">KG</text>
  </svg>
</body>
</html>
```